Backerline Unfiltered Podcast Artwork Needed

I run a podcast: Backerline Unfiltered.

Here's the website: backerlineunfiltered.example.

I'm looking for new artwork (minimum 1400x1400px).

My brand colors: #ff6600 and/or ##00c4cc

I'd LOVE to incorporate my image, my name (Marisella Dunford).

I want it to be fun, but serious. Also, bonus for coming up with a good incorporated logo on the artwork. I can't stand mine!!

Ones I love the look of... Owen Halbrook Show, Venture Chats with Bernard Eskew, Garrett Pimble.

Target Market(s)

Startups, Fundhatch, Physical Product Creators, millennials

Industry/Entity Type

Marketing

Font styles to use
Sans Serif

Requirements
Must have
• My photo, incorporate either color: #ff6600 OR #00c4cc
Nice to have
• I'm open!
Should not have
• Needs my photo!

```html
<!DOCTYPE html>
<html lang="en">
<head>
<meta charset="utf-8">
<title>Marisella Dunford — Podcast Artwork</title>
<link rel="stylesheet" href="https://fonts.googleapis.com/css2?family=PT+Serif:wght@700&display=swap">
<style>
  :root {
    --brand-orange: #ff6600;
    --brand-teal: #00c4cc;
    --band-white: #f7f7f7;
    --metal-dark: #161616;
    --metal-mid: #2c2c2c;
    --metal-line: #3a3a3a;
    --sun-light: #fff6d8;
    --foliage: #7f8a2c;
    --foliage-deep: #4f5a1c;
    --top-plum: #4a2436;
    --skin-warm: #e8b48a;
  }
  html, body {
    margin: 0;
    padding: 0;
    width: 1200px;
    height: 1200px;
    overflow: hidden;
    background: #ffffff;
  }
  .artwork {
    position: relative;
    width: 1200px;
    height: 1200px;
    overflow: hidden;
  }
  .artwork svg {
    display: block;
    width: 1200px;
    height: 1200px;
  }
  .host-name {
    font-family: "PT Serif", Georgia, serif;
    font-weight: 700;
  }
  .host-name--first { fill: var(--brand-teal); font-size: 132px; }
  .host-name--last { fill: var(--band-white); font-size: 128px; }
  .band--orange { fill: var(--brand-orange); }
  .band--teal { fill: var(--brand-teal); }
  .band--white { fill: var(--band-white); }
  .metal-lines line { stroke: var(--metal-line); stroke-width: 1.5; opacity: 0.7; }
</style>
</head>
<body>
<main class="artwork">
  <svg viewBox="0 0 1200 1200" xmlns="http://www.w3.org/2000/svg">
    <defs>
      <radialGradient id="sunlitScene" cx="0.55" cy="0.05" r="0.9">
        <stop offset="0" stop-color="var(--sun-light)"/>
        <stop offset="0.35" stop-color="#d8cc7a"/>
        <stop offset="0.65" stop-color="var(--foliage)"/>
        <stop offset="1" stop-color="var(--foliage-deep)"/>
      </radialGradient>
      <linearGradient id="hostPortrait" x1="0" y1="0" x2="0" y2="1">
        <stop offset="0" stop-color="#d9a165"/>
        <stop offset="0.4" stop-color="var(--skin-warm)"/>
        <stop offset="0.52" stop-color="var(--top-plum)"/>
        <stop offset="1" stop-color="#3a1c2b"/>
      </linearGradient>
      <linearGradient id="brushedMetal" x1="0" y1="0" x2="1" y2="1">
        <stop offset="0" stop-color="var(--metal-mid)"/>
        <stop offset="0.5" stop-color="var(--metal-dark)"/>
        <stop offset="0.75" stop-color="#262626"/>
        <stop offset="1" stop-color="#0e0e0e"/>
      </linearGradient>
      <clipPath id="metalClip">
        <polygon points="450,990 1200,454 1200,1200 450,1200"/>
      </clipPath>
    </defs>

    <!-- outdoor backdrop -->
    <rect class="scene-backdrop" x="0" y="0" width="1200" height="1200" fill="url(#sunlitScene)"
          role="img" aria-label="Sunlit outdoor backdrop of trees and water, softly blurred"/>

    <!-- diagonal brand bands -->
    <g class="brand-bands">
      <polygon class="band--orange" points="450,426 1037,0 1200,0 1200,193 450,727"/>
      <polygon class="band--teal" points="450,727 1200,193 1200,360 450,903"/>
      <polygon class="band--white" points="450,903 1200,360 1200,454 450,990"/>
      <polygon class="band--metal" points="450,990 1200,454 1200,1200 450,1200" fill="url(#brushedMetal)"/>
      <g class="metal-lines" clip-path="url(#metalClip)">
        <line x1="300" y1="1150" x2="1300" y2="435"/>
        <line x1="300" y1="1230" x2="1300" y2="515"/>
        <line x1="300" y1="1310" x2="1300" y2="595"/>
        <line x1="300" y1="1390" x2="1300" y2="675"/>
        <line x1="300" y1="1470" x2="1300" y2="755"/>
        <line x1="300" y1="1550" x2="1300" y2="835"/>
        <line x1="300" y1="1630" x2="1300" y2="915"/>
        <line x1="300" y1="1710" x2="1300" y2="995"/>
        <line x1="300" y1="1790" x2="1300" y2="1075"/>
        <line x1="300" y1="1870" x2="1300" y2="1155"/>
      </g>
    </g>

    <!-- host portrait -->
    <rect class="host-portrait" x="30" y="150" width="570" height="1050" rx="200" ry="200"
          fill="url(#hostPortrait)"
          role="img" aria-label="Photo of the host, smiling, in a plum sleeveless top"/>

    <!-- host name -->
    <text class="host-name host-name--first" x="583" y="617" transform="rotate(-35.8 583 617)">Marisella</text>
    <text class="host-name host-name--last" x="1190" y="330" text-anchor="end" transform="rotate(-35.8 1190 330)">Dunford</text>
  </svg>
</main>
</body>
</html>
```